Tincture Design for Woman Owned CBD Branf

LumiVelle is a luxery CBD brand for millennial women.

Our premium L Oil contains 500mg of full spectrum CBD derived from specially-sourced hemp for unparalleled purity and quality. Each dropper delivers approximately 20mg of CBD. Available in two flavors, Natural and Mint.

The goal is to design an aesthetically pleasing tincture (bottle dropper) with label and box. The final design should coincide with our brand guidelines and easily marketed for beauty consumers. We are looking for a clean design, the use of raised fonts and/or metallic is fine.

We have 4 other designs we'd like to work on with the winning designer.

Target Market(s)

Millennial Women, Income $75k+

Font styles to use
Other font styles liked:
• See Branding Sheet

Requirements
Must have
• Must follow brand guidelines (see attached for colors, font, etc)
Nice to have
• Raised font or Metallic Print

```html
<!DOCTYPE html>
<html lang="en">
<head>
<meta charset="utf-8">
<title>LumiVelle CBD Tinctures – Box and Label</title>
<link rel="stylesheet" href="https://fonts.googleapis.com/css2?family=Open+Sans:wght@400;600&display=swap">
<style>
  :root {
    --backdrop: #b7b5b6;
    --paper-top: #eeedea;
    --paper-bottom: #fbfbfa;
    --brand-green: #0f5e4c;
    --copper: #c8703f;
    --white: #ffffff;
  }
  * { margin: 0; padding: 0; box-sizing: border-box; }
  html, body {
    width: 1200px; height: 808px; overflow: hidden;
    background: var(--backdrop);
    font-family: "Open Sans", Arial, sans-serif;
  }
  .canvas { position: relative; width: 1200px; height: 808px; }

  .panel { position: absolute; overflow: hidden; }
  .panel-texture {
    position: absolute; inset: 0;
    background: linear-gradient(165deg, var(--paper-top) 0%, #f3f2ef 55%, var(--paper-bottom) 100%);
  }
  .centered {
    position: absolute; left: 0; right: 0; text-align: center;
    transform: translateY(-50%); white-space: nowrap;
  }
  .brand-name { color: var(--brand-green); font-weight: 600; letter-spacing: 0.5px; }
  .product-cbd { color: var(--brand-green); font-weight: 600; }
  .product-title { color: var(--brand-green); font-weight: 600; letter-spacing: -0.3px; }
  .product-sub { color: var(--brand-green); font-weight: 400; }
  .dose { color: var(--brand-green); font-weight: 400; }
  .tagline { color: var(--copper); font-weight: 400; }
  .rule { position: absolute; height: 2px; background: var(--copper); }
  .supplement-tab {
    position: absolute; bottom: 0;
    background: var(--brand-green); color: var(--white);
    display: flex; align-items: center; justify-content: center;
    white-space: nowrap;
  }

  /* Box front */
  .box-front { left: 335px; top: 64px; width: 250px; height: 656px; box-shadow: 0 2px 6px rgba(0,0,0,0.08); }
  .box-front .brand-name { top: 198px; font-size: 34px; }
  .box-front .product-cbd { top: 356px; font-size: 33px; }
  .box-front .product-sub { top: 379px; font-size: 7px; }
  .box-front .product-title { top: 402px; font-size: 36px; }
  .box-front .dose { top: 423px; font-size: 13px; }
  .box-front .rule-upper-left { left: 31px; width: 55px; top: 378px; }
  .box-front .rule-upper-right { left: 162px; width: 55px; top: 378px; }
  .box-front .rule-lower-left { left: 31px; width: 55px; top: 423px; }
  .box-front .rule-lower-right { left: 162px; width: 55px; top: 423px; }
  .box-front .tagline { top: 548px; font-size: 9.5px; letter-spacing: 0.1px; }
  .box-front .supplement-tab { left: 44px; width: 161px; height: 44px; border-radius: 26px 26px 0 0; font-size: 9.5px; }

  /* Bottle label */
  .bottle-label { left: 642px; top: 415px; width: 197px; height: 229px; }
  .bottle-label .brand-name { top: 53px; font-size: 19px; }
  .bottle-label .product-cbd { top: 106px; font-size: 17px; }
  .bottle-label .product-sub { top: 119px; font-size: 3.8px; }
  .bottle-label .product-title { top: 132px; font-size: 19.5px; }
  .bottle-label .dose { top: 144px; font-size: 7px; }
  .bottle-label .rule { height: 1.2px; }
  .bottle-label .rule-upper-left { left: 48px; width: 30px; top: 118.5px; }
  .bottle-label .rule-upper-right { left: 120px; width: 29px; top: 118.5px; }
  .bottle-label .rule-lower-left { left: 48px; width: 30px; top: 143.5px; }
  .bottle-label .rule-lower-right { left: 120px; width: 29px; top: 143.5px; }
  .bottle-label .tagline { top: 171px; font-size: 5.2px; }
  .bottle-label .supplement-tab { left: 51px; width: 96px; height: 22px; border-radius: 12px 12px 0 0; font-size: 5.4px; }
</style>
</head>
<body>
<main class="canvas">

  <section class="panel box-front" aria-label="Box front panel">
    <div class="panel-texture" role="img" aria-label="Soft off-white background with faint diagonal curved line pattern"></div>
    <p class="centered brand-name">LumiVelle</p>
    <p class="centered product-cbd">CBD</p>
    <span class="rule rule-upper-left"></span>
    <p class="centered product-sub">SOURCED HEMP</p>
    <span class="rule rule-upper-right"></span>
    <p class="centered product-title">TINCTURES</p>
    <span class="rule rule-lower-left"></span>
    <p class="centered dose">20mg</p>
    <span class="rule rule-lower-right"></span>
    <p class="centered tagline">FOR UNPARALLELED PURITY AND QUALITY</p>
    <div class="supplement-tab">DETTARY SUPPLEMENT&nbsp;&nbsp;30ML</div>
  </section>

  <section class="panel bottle-label" aria-label="Bottle label">
    <div class="panel-texture" role="img" aria-label="Soft off-white background with faint diagonal curved line pattern"></div>
    <p class="centered brand-name">LumiVelle</p>
    <p class="centered product-cbd">CBD</p>
    <span class="rule rule-upper-left"></span>
    <p class="centered product-sub">SOURCED HEMP</p>
    <span class="rule rule-upper-right"></span>
    <p class="centered product-title">TINCTURES</p>
    <span class="rule rule-lower-left"></span>
    <p class="centered dose">20mg</p>
    <span class="rule rule-lower-right"></span>
    <p class="centered tagline">FOR UNPARALLELED PURITY AND QUALITY</p>
    <div class="supplement-tab">DETTARY SUPPLEMENT&nbsp;&nbsp;30ML</div>
  </section>

</main>
</body>
</html>
```